New Web Design Project for kitchen company

We need a homepage mockup for a company that sells and installs kitchen and baths. Use your creative talent to come up with something visually appeal and professional for this web-site.

Please see the attached brief.

If you have any questions feel free to post them right on the project discussion.

Target Market(s)

homeowners

Number of Pages Required

1 page

Font styles to use
Serif
Other font styles liked:
• Something similar to the logo

```html
<!DOCTYPE html>
<html lang="en">
<head>
<meta charset="utf-8">
<title>Harborline Kitchen and Bath</title>
<link href="https://fonts.googleapis.com/css2?family=DM+Serif+Display&family=Nunito+Sans:ital,wght@0,300;0,400;0,600;0,700;1,400&display=swap" rel="stylesheet">
<style>
:root{
  --orange:#f0832a;
  --orange-light:#f6a565;
  --navy:#272c4d;
  --navy-deep:#1f2440;
  --blue:#2c4192;
  --text:#3b3f52;
  --muted:#7b7f8e;
  --white:#ffffff;
  --faint:#f4f4f6;
}
*{box-sizing:border-box;margin:0;padding:0}
html,body{width:1200px;height:4299px;overflow:hidden}
body{position:relative;background:var(--white);font-family:"Nunito Sans",Arial,sans-serif;color:var(--text)}
.abs{position:absolute}
.serif{font-family:"DM Serif Display",Georgia,serif;font-weight:400}
.photo{position:absolute}
.btn{position:absolute;background:var(--orange);color:var(--white);font-size:13px;font-weight:700;text-transform:uppercase;display:flex;align-items:center;justify-content:center;box-shadow:0 6px 14px rgba(240,131,42,.35)}
.btn::after{content:"";position:absolute;right:10px;top:50%;width:10px;height:10px;border-top:3px solid rgba(255,255,255,.45);border-right:3px solid rgba(255,255,255,.45);transform:translateY(-50%) rotate(45deg)}

/* header & hero */
.hero{left:0;top:0;width:1200px;height:674px;background:linear-gradient(160deg,#5a6488 0%,#3f4a73 45%,#2a3158 100%)}
.hero-overlay{left:0;top:0;width:1200px;height:674px;background:rgba(40,48,95,.35)}
.brand{left:28px;top:16px;display:flex;align-items:center;gap:10px;color:var(--white);font-family:"DM Serif Display",Georgia,serif;font-size:20px}
.brand-mark{width:30px;height:30px;border:2px solid var(--white);border-radius:50%}
.nav{right:26px;top:24px;display:flex;gap:24px;font-size:14px;font-weight:600;color:var(--white)}
.nav .active{border-bottom:3px solid var(--orange);padding-bottom:2px}
.hero-title{left:0;width:1200px;top:218px;text-align:center;color:var(--white);font-size:54px;line-height:61px}
.hero-sub{left:0;width:1200px;top:350px;text-align:center;color:var(--white);font-size:22px}

/* section heading */
.sec-title{font-size:36px;color:var(--navy)}
.sec-title em{font-style:normal;color:var(--orange)}
.rule{height:3px;background:var(--orange)}
.ghost{font-family:"DM Serif Display",Georgia,serif;color:var(--faint);font-size:120px;line-height:1;white-space:nowrap}

/* projects */
.project-card{position:absolute;width:398px;height:226px;background:var(--white);box-shadow:0 10px 30px rgba(30,35,70,.12);padding:18px 24px}
.project-card h3{font-weight:400;color:var(--orange);font-size:24px;margin-bottom:10px}
.project-card p{font-size:13px;line-height:19.5px;color:var(--text)}
.project-card .more{position:absolute;bottom:18px;font-size:13px;color:var(--orange);font-weight:600}
.project-card.right{text-align:right}
.project-card.right .more{right:24px}
.project-card.left .more{left:24px}
.card-band{position:absolute;height:5px;background:var(--orange-light);opacity:.7}
.arrows{position:absolute;width:81px;height:33px;background:var(--orange);display:flex;justify-content:space-around;align-items:center}
.arrows svg{width:14px;height:14px}

/* services */
.services-panel{left:890px;top:2432px;width:310px;height:474px;background:linear-gradient(180deg,#4b5476,#2e3558)}
.frame{position:absolute;background:var(--white);padding:7px;box-shadow:0 10px 30px rgba(20,25,50,.25)}
.frame .photo{position:static;width:100%;height:100%}
.body-copy{font-size:13.5px;line-height:19.5px;color:var(--text)}
.body-copy p{margin-bottom:9px}

/* cta */
.cta{left:0;top:2906px;width:1200px;height:122px;background:linear-gradient(90deg,#2c3f90 0%,#283a80 50%,#262f58 100%)}
.cta-text{left:0;width:980px;top:2950px;text-align:center;color:var(--white);font-size:26px;font-weight:400}

/* about */
.about-panel{left:0;top:3028px;width:335px;height:474px;background:linear-gradient(180deg,#3f4870,#2a3055)}

/* testimonials */
.quote-mark{position:absolute;color:var(--orange);font-family:"DM Serif Display",Georgia,serif;font-size:90px;line-height:1}
.t-card{position:absolute;background:var(--white);box-shadow:0 8px 26px rgba(30,35,70,.1);padding:26px 16px;font-style:italic;font-size:13px;line-height:19px;color:var(--muted)}
.t-card .who{font-style:normal;font-family:"DM Serif Display",Georgia,serif;font-size:10px;margin-top:12px;display:flex;align-items:center;gap:8px}
.t-card .who::before{content:"";width:14px;height:2px;background:var(--orange)}
.t-card.featured{background:var(--navy);color:var(--white);font-size:13.5px;line-height:19.5px;padding:24px 20px}
.t-card.featured .who{font-size:15px;color:var(--white)}

/* footer */
.footer{left:0;top:4078px;width:1200px;height:221px;background:var(--navy-deep)}
.foot-head{font-family:"DM Serif Display",Georgia,serif;color:var(--white);font-size:19px}
.foot-line{display:flex;align-items:center;gap:14px;color:var(--white);font-size:13px}
.social{display:flex;gap:20px;align-items:center}
.social span{width:44px;height:44px;display:flex;align-items:center;justify-content:center}
.social span i{display:block;width:18px;height:18px;border:2px solid var(--white)}
.social .hi{background:var(--blue)}
.links{right:102px;top:4143px;text-align:right;color:var(--white);font-size:13px;line-height:20px}
.copy{left:0;width:1200px;top:4272px;text-align:center;color:#c9cbd6;font-size:12px}
</style>
</head>
<body>

<!-- header / hero -->
<div class="photo hero" role="img" aria-label="Bright remodeled kitchen with white cabinets, granite counters and blue patterned rug"></div>
<div class="abs hero-overlay"></div>
<div class="abs brand"><span class="brand-mark"></span>HARBORLINE</div>
<nav class="abs nav"><span class="active">HOME</span><span>PROJECTS</span><span>ABOUT US</span><span>CONTACT US</span></nav>
<h1 class="abs hero-title serif">Welcome to Harborline<br>Kitchen and Bath</h1>
<div class="abs hero-sub">Committed To Quality</div>
<div class="btn" style="left:504px;top:399px;width:190px;height:28px">Explore our work</div>

<!-- projects -->
<div class="abs ghost" style="left:-10px;top:695px">Projects</div>
<h2 class="abs sec-title serif" style="left:0;width:1200px;text-align:center;top:720px">Recent <em>Projects</em></h2>
<div class="abs rule" style="left:566px;top:777px;width:68px"></div>

<div class="photo" style="left:189px;top:813px;width:482px;height:340px;background:linear-gradient(135deg,#8a8580,#c9c2b6 45%,#6b513c)" role="img" aria-label="Kitchen with white island, dark counters and stainless wall ovens"></div>
<div class="arrows" style="left:189px;top:1120px"><svg viewBox="0 0 14 14"><path d="M9 2 4 7l5 5" fill="none" stroke="#fff" stroke-width="2"/></svg><svg viewBox="0 0 14 14"><path d="m5 2 5 5-5 5" fill="none" stroke="#fff" stroke-width="2"/></svg></div>
<div class="project-card left" style="left:613px;top:876px"><h3>Hale's Kitchen</h3><p>Lorem ipsum dolor sit amet, consectetur adipiscing elit. Cras ut feugiat odio, sit amet laoreet lorem. Quisque at erat tempor sapien auctor accumsan vitae eget tellus. Aliquam erat volutpat. Integer efficitur erat mi, in pellentesque erat malesuada vitae.</p><span class="more">Show More &nbsp;⟶</span></div>
<div class="card-band" style="left:613px;top:1102px;width:398px"></div>

<div class="photo" style="left:529px;top:1198px;width:482px;height:339px;background:linear-gradient(135deg,#b9bcc0,#e3e1dc 40%,#4d5470 80%,#2e4c86)" role="img" aria-label="Open kitchen with grey island, pendant lights and living room sofa"></div>
<div class="arrows" style="left:930px;top:1504px"><svg viewBox="0 0 14 14"><path d="M9 2 4 7l5 5" fill="none" stroke="#fff" stroke-width="2"/></svg><svg viewBox="0 0 14 14"><path d="m5 2 5 5-5 5" fill="none" stroke="#fff" stroke-width="2"/></svg></div>
<div class="project-card right" style="left:187px;top:1263px"><h3>Corwin Kitchen Remodel</h3><p>Lorem ipsum dolor sit amet, consectetur adipiscing elit. Cras ut feugiat odio, sit amet laoreet lorem. Quisque at erat tempor sapien auctor accumsan vitae eget tellus. Aliquam erat volutpat. Integer efficitur erat mi, in pellentesque erat malesuada vitae.</p><span class="more">Show More &nbsp;⟶</span></div>
<div class="card-band" style="left:195px;top:1485px;width:389px"></div>

<div class="photo" style="left:189px;top:1582px;width:482px;height:341px;background:linear-gradient(135deg,#cfcbc3,#eae6de 40%,#4e4a47 75%,#6a1e22)" role="img" aria-label="White kitchen with dark grey island and red stools"></div>
<div class="arrows" style="left:189px;top:1890px"><svg viewBox="0 0 14 14"><path d="M9 2 4 7l5 5" fill="none" stroke="#fff" stroke-width="2"/></svg><svg viewBox="0 0 14 14"><path d="m5 2 5 5-5 5" fill="none" stroke="#fff" stroke-width="2"/></svg></div>
<div class="project-card left" style="left:613px;top:1647px"><h3>Owen and Clara's Kitchen</h3><p>Lorem ipsum dolor sit amet, consectetur adipiscing elit. Cras ut feugiat odio, sit amet laoreet lorem. Quisque at erat tempor sapien auctor accumsan vitae eget tellus. Aliquam erat volutpat. Integer efficitur erat mi, in pellentesque erat malesuada vitae.</p><span class="more">Show More &nbsp;⟶</span></div>
<div class="card-band" style="left:613px;top:1873px;width:398px"></div>

<div class="photo" style="left:529px;top:1968px;width:482px;height:340px;background:linear-gradient(135deg,#d7dade,#f1efea 40%,#5b5650 75%,#2b4e8c)" role="img" aria-label="Kitchen with wood island, yellow kettle and blue rug"></div>
<div class="arrows" style="left:930px;top:2275px"><svg viewBox="0 0 14 14"><path d="M9 2 4 7l5 5" fill="none" stroke="#fff" stroke-width="2"/></svg><svg viewBox="0 0 14 14"><path d="m5 2 5 5-5 5" fill="none" stroke="#fff" stroke-width="2"/></svg></div>
<div class="project-card right" style="left:187px;top:2033px"><h3>Mark and Elise's Bathroom</h3><p>Lorem ipsum dolor sit amet, consectetur adipiscing elit. Cras ut feugiat odio, sit amet laoreet lorem. Quisque at erat tempor sapien auctor accumsan vitae eget tellus. Aliquam erat volutpat. Integer efficitur erat mi, in pellentesque erat malesuada vitae.</p><span class="more">Show More &nbsp;⟶</span></div>
<div class="card-band" style="left:195px;top:2256px;width:389px"></div>

<div class="btn" style="left:504px;top:2353px;width:192px;height:34px">Explore our work</div>

<!-- services -->
<div class="abs ghost" style="left:0;top:2475px">Services</div>
<div class="abs services-panel"></div>
<div class="frame" style="left:639px;top:2490px;width:479px;height:356px"><div class="photo" style="background:linear-gradient(135deg,#8d7a55,#e6dfcf 45%,#c99a5a)" role="img" aria-label="Cream kitchen cabinetry with built-in bookshelf and wood floor"></div></div>
<h2 class="abs sec-title serif" style="left:122px;top:2550px">Our <em>Services</em></h2>
<div class="abs rule" style="left:347px;top:2572px;width:71px"></div>
<div class="abs body-copy" style="left:122px;top:2616px;width:485px">
<p>At Harborline Kitchen and Bath, we are a full-service kitchen and bath design, sales, and installation firm. With over 35 years of industry experience, Harborline has become the #1 most recommended kitchen and bath remodeling company in the Metro-West and Greater Boston area.</p>
<p>We can manage your entire remodeling project from start to finish; or work with your contractor to design and assist in installation of your kitchen or bath.</p>
<p>We take great pride in our work and our happy clients!</p>
</div>

<!-- cta -->
<div class="abs cta"></div>
<div class="abs cta-text">Schedule your in-home consultation today !</div>
<div class="btn" style="left:830px;top:2949px;width:143px;height:35px">Pick a date</div>

<!-- about -->
<div class="abs ghost" style="left:820px;top:3065px">About</div>
<div class="abs about-panel"></div>
<div class="frame" style="left:100px;top:3088px;width:481px;height:355px"><div class="photo" style="background:linear-gradient(135deg,#cbc6bc,#efebe3 40%,#4c4845 75%,#6a1e22)" role="img" aria-label="Kitchen with large island, pendant lights and red stools"></div></div>
<h2 class="abs sec-title serif" style="left:611px;top:3133px">About <em>Harborline</em></h2>
<div class="abs rule" style="left:908px;top:3156px;width:70px"></div>
<div class="abs body-copy" style="left:611px;top:3203px;width:480px">
<p>Our 30th Year in the Kitchen and Bath Industry!</p>
<p>In 1989, Ray and Lena Marchetti started Harborline Kitchens out of a small storefront in Eastbrook, MA. In order to find more room for their growing business, they moved their showroom to its current location in Westfield Hills, MA. 30 years and thousands of happy clients later, Harborline Kitchen and Bath is still committed to exceptional quality of work and design.</p>
<p>In early 2019, Ray Dolan was brought on to continue the rich tradition of Harborline and work along Ray Marchetti. Both Ray's are looking forward to the next chapter in Harborline!</p>
</div>

<!-- testimonials -->
<h2 class="abs sec-title serif" style="left:0;width:1200px;text-align:center;top:3550px">Testimonials</h2>
<div class="abs rule" style="left:566px;top:3604px;width:68px"></div>

<div class="quote-mark" style="left:126px;top:3660px;font-size:70px">“</div>
<div class="t-card" style="left:113px;top:3689px;width:279px;height:242px">Harborline Kitchens Inc. had done an awesome remodeling of my wife's kitchen several years ago so I called on them to remodel my bathroom as it was in need of a lot of work. Ray and his crew of professionals came in and did an amazing job. Ray and his wife helped pick out just the right vanity, knobs, countertop and flooring to match. They coordinated the<div class="who">Mara Whitcomb</div></div>

<div class="t-card featured" style="left:407px;top:3655px;width:387px;height:311px">Harborline Kitchens Inc. had done an awesome remodeling of my wife's kitchen several years ago so I called on them to remodel my bathroom as it was in need of a lot of work. Ray and his crew of professionals came in and did an amazing job. Ray and his wife helped pick out just the right vanity, knobs, countertop and flooring to match. They coordinated the carpenter, plumber, electrician and plaster. He kept in contact throughout the whole remodeling process. If you're looking to get an excellent remodeling at a reasonable price call Harborline Kitchens you will not be disappointed.<div class="who">Mara Whitcomb</div></div>
<div class="quote-mark" style="left:424px;top:3615px">“</div>

<div class="quote-mark" style="left:800px;top:3660px;font-size:70px">“</div>
<div class="t-card" style="left:803px;top:3689px;width:284px;height:242px">Harborline Kitchens Inc. had done an awesome remodeling of my wife's kitchen several years ago so I called on them to remodel my bathroom as it was in need of a lot of work. Ray and his crew of professionals came in and did an amazing job. Ray and his wife helped pick out just the right vanity, knobs, countertop and flooring to match. They coordinated the<div class="who">Mara Whitcomb</div></div>

<div class="arrows" style="left:557px;top:3997px;width:84px;height:34px"><svg viewBox="0 0 14 14"><path d="M9 2 4 7l5 5" fill="none" stroke="#fff" stroke-width="2"/></svg><svg viewBox="0 0 14 14"><path d="m5 2 5 5-5 5" fill="none" stroke="#fff" stroke-width="2"/></svg></div>

<!-- footer -->
<footer class="abs footer"></footer>
<div class="abs foot-head" style="left:102px;top:4102px">Contact Us</div>
<div class="abs foot-line" style="left:102px;top:4143px"><svg width="20" height="14" viewBox="0 0 20 14"><rect x="1" y="1" width="18" height="12" fill="#fff"/><path d="M1 1l9 7 9-7" fill="none" stroke="#1f2440" stroke-width="1.5"/></svg>rayd@harborlinekb.com</div>
<div class="abs foot-line" style="left:102px;top:4180px"><svg width="20" height="16" viewBox="0 0 20 16"><path d="M4 1l3 3-2 2c1 2 3 4 5 5l2-2 3 3-2 2C8 14 2 8 2 3z" fill="#fff"/></svg>555-014-2290</div>
<div class="abs foot-head" style="left:0;width:1192px;text-align:center;top:4100px">Follow Us</div>
<div class="abs social" style="left:510px;top:4143px">
<span class="hi"><i style="border-radius:50%"></i></span><span><i style="border-radius:4px"></i></span><span><i style="border-radius:50%"></i></span>
</div>
<div class="abs links">Imprint<br>Privacy Policy</div>
<div class="abs copy">© Copyright 2020 &nbsp;Harborline. All rights reserved.</div>

</body>
</html>
```